New Webpage for High Class Expert Witness Services Company

We are looking for a minimalist design for a webpage that just has our logo and an entry form offer to connect with one of our Liaisons.
The entry form should just ask for Name, Email, Contact Info and Description of Project.

Company Name is: The Marlow Crest Advisory Services

Number of Pages Required

1 page

```html
<!DOCTYPE html>
<html lang="en">
<head>
<meta charset="utf-8">
<title>Marlow Crest Advisory Services — Connect With Our Liaison</title>
<link href="https://fonts.googleapis.com/css2?family=Cinzel:wght@400&family=Libre+Caslon+Text:wght@400&family=Montserrat:wght@300;400;500&display=swap" rel="stylesheet">
<style>
  :root {
    --bg: #121212;
    --bg-glow: #2e2e2e;
    --text-main: #ececec;
    --text-soft: #b9b9b9;
    --text-dim: #9a9a9a;
    --line: #4a4a4a;
    --panel: #161616;
    --panel-line: #2c2c2c;
    --gold-top: #a07f4a;
    --gold-bottom: #6e5128;
    --gold-edge: #c7a46a;
  }
  * { margin: 0; padding: 0; box-sizing: border-box; }
  html, body { width: 800px; height: 1200px; overflow: hidden; }
  body {
    position: relative;
    background: radial-gradient(ellipse 260px 320px at 330px 560px, var(--bg-glow), var(--bg) 100%);
    background-color: var(--bg);
    color: var(--text-main);
    font-family: "Montserrat", sans-serif;
  }
  .brand {
    position: absolute; left: 56px; top: 272px;
    display: flex; align-items: center; gap: 14px;
  }
  .brand-mark { width: 52px; height: 52px; background: #9c9c9c; }
  .brand-name {
    font-family: "Cinzel", serif; font-weight: 400; font-size: 17px;
    line-height: 1.25; letter-spacing: 1.5px; color: #d6d6d6; width: 300px;
  }
  .brand-tagline {
    position: absolute; left: 56px; top: 334px;
    font-family: "Cinzel", serif; font-size: 9px; letter-spacing: 2.4px; color: var(--text-dim);
  }
  .headline {
    position: absolute; left: 55px; top: 380px;
    font-family: "Libre Caslon Text", serif; font-weight: 400;
    font-size: 40px; line-height: 47px; color: var(--text-main);
  }
  .subline {
    position: absolute; left: 56px; top: 536px;
    font-weight: 300; font-size: 16px; line-height: 26px; color: var(--text-soft);
  }
  .liaison-form {
    position: absolute; left: 459px; top: 323px; width: 298px; height: 476px;
    background: var(--panel); border: 1px solid var(--panel-line); border-radius: 3px;
    box-shadow: 0 10px 40px rgba(0,0,0,0.5);
  }
  .form-title {
    position: absolute; top: 32px; left: 0; right: 0; text-align: center;
    font-size: 11.5px; letter-spacing: 2.2px; font-weight: 400; color: #d0d0d0;
  }
  .field {
    position: absolute; left: 22px; width: 253px; height: 34px;
    border: 1px solid var(--line); border-radius: 2px; background: transparent;
    padding: 0 13px; font-family: inherit; font-size: 13px; font-weight: 300; color: var(--text-soft);
    line-height: 32px;
  }
  .field-name { top: 67px; }
  .field-email { top: 118px; }
  .field-phone { top: 169px; }
  .field-project { top: 220px; height: 91px; line-height: 1; padding-top: 10px; }
  .submit {
    position: absolute; left: 22px; top: 335px; width: 253px; height: 40px;
    border: 1px solid var(--gold-edge); border-radius: 3px;
    background: linear-gradient(var(--gold-top), var(--gold-bottom));
    color: #f3ece0; font-family: inherit; font-size: 15.5px; font-weight: 500; letter-spacing: 0.3px;
    box-shadow: 0 4px 14px rgba(0,0,0,0.6);
  }
  .assurance {
    position: absolute; display: flex; align-items: center; gap: 6px;
    font-size: 12px; font-weight: 300; color: var(--text-soft);
  }
  .assurance svg { stroke: #aaa; fill: none; stroke-width: 1.2; }
  .a-confidential { left: 17px; top: 401px; }
  .a-legal { left: 139px; top: 401px; }
  .a-medical { left: 76px; top: 437px; }
  .assurance-divider {
    position: absolute; left: 10px; right: 10px; top: 423px; height: 1px; background: #232323;
  }
  .contact-email {
    position: absolute; top: 834px; left: 0; width: 804px; text-align: center;
    font-family: "Libre Caslon Text", serif; font-size: 16px; letter-spacing: 0.6px; color: var(--text-soft);
  }
  .contact-address {
    position: absolute; top: 878px; left: 0; width: 804px; text-align: center;
    font-size: 15px; font-weight: 300; letter-spacing: 0.6px; color: var(--text-soft);
  }
  .contact-address .sep { display: inline-block; width: 1px; height: 16px; background: #555; margin: 0 18px; vertical-align: middle; }
</style>
</head>
<body>
  <header class="brand">
    <div class="brand-mark"></div>
    <div class="brand-name">The Marlow Crest Advisory Services</div>
  </header>
  <p class="brand-tagline">SEAMLESS MEDICAL EXPERT INTEGRATION</p>

  <h1 class="headline">Expert Witness<br>Coordination,<br>Simplified.</h1>
  <p class="subline">Seamless medical expert integration<br>for legal defense teams.</p>

  <form class="liaison-form">
    <h2 class="form-title">CONNECT WITH OUR LIAISON</h2>
    <div class="field field-name">Name</div>
    <div class="field field-email">Email</div>
    <div class="field field-phone">Contact Number</div>
    <div class="field field-project">Description of Project</div>
    <button class="submit" type="button">Request Consultation</button>

    <div class="assurance a-confidential">
      <svg width="20" height="20" viewBox="0 0 20 20"><circle cx="10" cy="10" r="9" stroke="#333"/><rect x="6.5" y="9" width="7" height="6" fill="#bbb" stroke="none"/><path d="M7.8 9V7.3a2.2 2.2 0 0 1 4.4 0V9"/></svg>
      Confidential
    </div>
    <div class="assurance a-legal">
      <svg width="24" height="18" viewBox="0 0 24 18"><path d="M12 2v14M6 17h12M3 4h18M5 4l-3 7h6zM19 4l-3 7h6zM2 11a3 2 0 0 0 6 0M16 11a3 2 0 0 0 6 0"/></svg>
      Legal Focused
    </div>
    <div class="assurance-divider"></div>
    <div class="assurance a-medical">
      <svg width="16" height="18" viewBox="0 0 16 18"><path d="M8 1v16M3 4h10M5 7c3 1 6 2 0 4M11 7c-3 1-6 2 0 4"/></svg>
      Medical Expertise
    </div>
  </form>

  <footer>
    <p class="contact-email">info@marlowcrestadvisory.com</p>
    <p class="contact-address">1234 Main St, Suite 400<span class="sep"></span>City, State 12345</p>
  </footer>
</body>
</html>
```